Marrowgate Auctions Business Cards Design Needed

I need a business card design that is modern looking - double sided (maybe just my logo on the back, but open to suggestions) - the overall design is up to you. I want it to be easy to read - not over the top flashy. I already have a company logo which I uploaded so that needs to be used. The colors of my logo are the colors I want on the card... so blue and gray (do need to match the logo colors).

Requirements
Must have
• Would like the card to be sleek, modern and easy to ready

```html
<!DOCTYPE html>
<html lang="en">
<head>
<meta charset="utf-8">
<title>Marrowgate Auctions – Business Cards</title>
<link rel="stylesheet" href="https://fonts.googleapis.com/css2?family=Arimo:wght@400;700&display=swap">
<style>
  :root {
    --brand-blue: #2e76bd;
    --brand-gray: #55585c;
    --ink-gray: #3d4044;
    --card-white: #ffffff;
    --backdrop: #2b2b2d;
  }
  * { box-sizing: border-box; margin: 0; padding: 0; }
  html, body {
    width: 1200px; height: 880px; overflow: hidden;
    background: var(--backdrop);
    font-family: "Arimo", Arial, sans-serif;
  }
  .canvas { position: relative; width: 1200px; height: 880px; }

  .card {
    position: absolute;
    width: 700px; height: 400px;
    border-radius: 24px;
    overflow: hidden;
    box-shadow: 0 14px 30px rgba(0,0,0,.45);
  }

  /* Front card */
  .card-front {
    left: 60px; top: 30px;
    background: var(--brand-blue);
    display: flex; flex-direction: column;
    align-items: center; justify-content: center;
    color: var(--card-white);
  }
  .card-front .company-name {
    font-weight: 700; font-size: 46px; letter-spacing: 0.5px;
    text-transform: uppercase;
  }
  .card-front .tagline {
    margin-top: 8px; font-size: 17px; letter-spacing: 0.6px;
  }

  /* Back card */
  .card-back {
    left: 440px; top: 455px;
    background: var(--card-white);
  }
  .card-back .wave { position: absolute; inset: 0; }
  .card-back .brand {
    position: absolute; left: 40px; top: 140px;
  }
  .card-back .company-name {
    font-weight: 700; font-size: 34px; line-height: 40px; color: var(--brand-blue);
    text-transform: uppercase; letter-spacing: 0.3px;
  }
  .card-back .tagline {
    margin-top: 2px; font-size: 14px; color: var(--ink-gray); letter-spacing: 0.4px;
  }
  .card-back .person {
    position: absolute; left: 40px; top: 222px;
  }
  .person-name { font-weight: 700; font-size: 22px; line-height: 26px; color: var(--brand-blue); }
  .person-title { font-size: 15px; color: var(--ink-gray); margin-top: 2px; }
  .divider {
    position: absolute; left: 40px; right: 40px; top: 282px;
    height: 1.5px; background: var(--brand-blue);
  }
  .website {
    position: absolute; right: 40px; top: 258px;
    font-weight: 700; font-size: 14px; color: var(--brand-blue);
  }
  .contact-list {
    position: absolute; left: 40px; top: 296px;
    list-style: none; font-size: 15px; color: var(--ink-gray);
  }
  .contact-list li { display: flex; align-items: center; gap: 8px; height: 24px; }
  .contact-icon { width: 18px; height: 18px; }
</style>
</head>
<body>
<main class="canvas">

  <section class="card card-front" aria-label="Business card front">
    <div class="company-name">Marrowgate Auctions</div>
    <div class="tagline">Improving Charity Auctions Nationwide</div>
  </section>

  <section class="card card-back" aria-label="Business card back">
    <svg class="wave" viewBox="0 0 700 400" width="700" height="400" aria-hidden="true">
      <path d="M0 0 H700 V140 C560 100 300 56 0 58 Z" fill="var(--brand-blue)"/>
      <path d="M18 76 C300 64 560 104 700 146 V164 C560 124 300 84 18 76 Z" fill="var(--brand-gray)"/>
    </svg>

    <div class="brand">
      <div class="company-name">Marrowgate Auctions</div>
      <div class="tagline">Improving Charity Auctions Nationwide</div>
    </div>

    <div class="person">
      <div class="person-name">Dana Whitlock</div>
      <div class="person-title">Owner/President - Auctioneer</div>
    </div>

    <div class="website">http://bidlantern.com/</div>
    <div class="divider"></div>

    <ul class="contact-list">
      <li>
        <svg class="contact-icon" viewBox="0 0 20 20" aria-hidden="true">
          <circle cx="10" cy="10" r="9" fill="none" stroke="var(--brand-blue)" stroke-width="1.6"/>
          <path d="M6.5 5.5 L8.5 5.5 L9.3 8 L8 9 C8.6 10.4 9.6 11.4 11 12 L12 10.7 L14.5 11.5 L14.5 13.5 C10 14 6 10 6.5 5.5 Z" fill="var(--brand-blue)"/>
        </svg>
        555-014-2287
      </li>
      <li>
        <svg class="contact-icon" viewBox="0 0 20 20" aria-hidden="true">
          <circle cx="10" cy="10" r="9" fill="none" stroke="var(--brand-blue)" stroke-width="1.6"/>
          <rect x="5" y="6.5" width="10" height="7" fill="none" stroke="var(--brand-blue)" stroke-width="1.4"/>
          <path d="M5 6.5 L10 10.5 L15 6.5" fill="none" stroke="var(--brand-blue)" stroke-width="1.4"/>
        </svg>
        hello@marrowgateauctions.com
      </li>
    </ul>
  </section>

</main>
</body>
</html>
```